Skin care manufacturer looking for packaging design for new skin care brand.

We need a design and logo for a skin care brand to be sold at retail stores and online in the United States and Europe. The design will be for 1.7oz - 2oz serums that will not have a retail box. The name of the brand is Velora Fen and should be a luxurious brand that is approachable. The brand will consist of 4 face serums - Vitamin C, Collagen, Retinol and Hyaluronic Acid that all contain Dead Sea Minerals. Images shown are for inspiration only. Color of bottles can be varied based on design and bottles can be screen printed or labeled.

```html
<!DOCTYPE html>
<html lang="en">
<head>
<meta charset="utf-8">
<title>Velora Fen — Serum Labels</title>
<link rel="stylesheet" href="https://fonts.googleapis.com/css2?family=Nunito:wght@900&family=Fjalla+One&family=Cormorant+Garamond:wght@500&family=Montserrat:wght@400;500&display=swap">
<style>
  :root {
    --page-bg: #eeeff1;
    --ink-white: #ffffff;
    --vitc-top: #f7a81c;
    --vitc-bottom: #5a2f08;
    --coll-top: #d35cf0;
    --coll-bottom: #5e1a6f;
    --ret-top: #7cc8f7;
    --ret-bottom: #1c3366;
    --hya-top: #8fd63a;
    --hya-bottom: #2c4a14;
  }
  * { margin: 0; padding: 0; box-sizing: border-box; }
  html, body { width: 1200px; height: 1200px; overflow: hidden; }
  body {
    background: var(--page-bg);
    display: flex;
    align-items: center;
    justify-content: center;
  }
  .label-row {
    display: flex;
    gap: 30px;
  }
  .serum-label {
    width: 250px;
    height: 440px;
    border-radius: 18px;
    padding: 54px 16px 40px;
    display: flex;
    flex-direction: column;
    align-items: center;
    color: var(--ink-white);
    text-align: center;
  }
  .serum-label--vitamin-c { background: linear-gradient(180deg, var(--vitc-top), var(--vitc-bottom)); }
  .serum-label--collagen { background: linear-gradient(180deg, var(--coll-top), var(--coll-bottom)); }
  .serum-label--retinol { background: linear-gradient(180deg, var(--ret-top), var(--ret-bottom)); }
  .serum-label--hyaluronic { background: linear-gradient(180deg, var(--hya-top), var(--hya-bottom)); }

  .brand-name {
    font-family: "Nunito", sans-serif;
    font-weight: 900;
    font-size: 44px;
    line-height: 1.02;
    letter-spacing: 0.5px;
    color: var(--ink-white);
  }
  .brand-name span { display: block; }
  .serum-type {
    margin-top: 22px;
    font-family: "Cormorant Garamond", serif;
    font-weight: 500;
    font-size: 11.5px;
    letter-spacing: 1.6px;
    text-transform: uppercase;
  }
  .product-box {
    margin-top: 6px;
    width: 100%;
    border: 1.5px solid var(--ink-white);
    padding: 6px 4px 16px;
    position: relative;
  }
  .product-name {
    font-family: "Fjalla One", sans-serif;
    font-size: 36px;
    line-height: 1.1;
    letter-spacing: -0.5px;
  }
  .product-name--long { font-size: 25px; line-height: 1.55; }
  .minerals-tag {
    position: absolute;
    left: 50%;
    bottom: -9px;
    transform: translateX(-50%);
    white-space: nowrap;
    background: var(--ink-white);
    padding: 1px 7px;
    font-family: "Montserrat", sans-serif;
    font-weight: 500;
    font-size: 9.5px;
    text-transform: uppercase;
    color: #3a2a10;
  }
  .volume {
    margin-top: 40px;
    font-family: "Montserrat", sans-serif;
    font-size: 11px;
  }
  .origin {
    margin-top: 6px;
    font-family: "Montserrat", sans-serif;
    font-size: 10px;
    letter-spacing: 4px;
  }
</style>
</head>
<body>
  <main class="label-row">
    <section class="serum-label serum-label--vitamin-c">
      <h2 class="brand-name"><span>VELORA</span><span>FEN</span></h2>
      <p class="serum-type">Advanced Anti Aging Serum</p>
      <div class="product-box">
        <p class="product-name">VITAMIN C</p>
        <p class="minerals-tag">With Dead Sea Minerals</p>
      </div>
      <p class="volume">2 FL OZ / 60 ML</p>
      <p class="origin">MADE IN USA</p>
    </section>

    <section class="serum-label serum-label--collagen">
      <h2 class="brand-name"><span>VELORA</span><span>FEN</span></h2>
      <p class="serum-type">Advanced Anti Aging Serum</p>
      <div class="product-box">
        <p class="product-name">COLLAGEN</p>
        <p class="minerals-tag">With Dead Sea Minerals</p>
      </div>
      <p class="volume">2 FL OZ / 60 ML</p>
      <p class="origin">MADE IN USA</p>
    </section>

    <section class="serum-label serum-label--retinol">
      <h2 class="brand-name"><span>VELORA</span><span>FEN</span></h2>
      <p class="serum-type">Advanced Anti Aging Serum</p>
      <div class="product-box">
        <p class="product-name">RETINOL</p>
        <p class="minerals-tag">With Dead Sea Minerals</p>
      </div>
      <p class="volume">2 FL OZ / 60 ML</p>
      <p class="origin">MADE IN USA</p>
    </section>

    <section class="serum-label serum-label--hyaluronic">
      <h2 class="brand-name"><span>VELORA</span><span>FEN</span></h2>
      <p class="serum-type">Advanced Anti Aging Serum</p>
      <div class="product-box">
        <p class="product-name product-name--long">HYALURONIC ACID</p>
        <p class="minerals-tag">With Dead Sea Minerals</p>
      </div>
      <p class="volume">2 FL OZ / 60 ML</p>
      <p class="origin">MADE IN USA</p>
    </section>
  </main>
</body>
</html>
```